1 Page Bio, describing our Mission to buy multifamily properties in Colorado Springs.

I am uploading a sample of an associate who is doing a similar thing in Tampa Florida. I will also upload an attempt by my assistant to make the flyer and I will upload 3 pictures to use, along with another document that has text to add. I want to be able to edit the document pretty easily inside a google doc. thanks, I want it to look clean and professional.

```html
<!DOCTYPE html>
<html lang="en">
<head>
<meta charset="utf-8">
<title>Multifamily Mission – Colorado Springs</title>
<link href="https://fonts.googleapis.com/css2?family=Lato:ital,wght@0,400;0,700;1,400;1,700;1,900&display=swap" rel="stylesheet">
<style>
  :root{
    --green-deep:#0b4a34;
    --green-mid:#0f7a48;
    --green-bright:#1fae57;
    --gold:#c98a3a;
    --gold-dark:#9c5f26;
    --panel:#e8e9eb;
    --ink:#4a4a4c;
    --white:#ffffff;
    --footer:#bdbdbf;
  }
  *{box-sizing:border-box;margin:0;padding:0}
  html,body{width:900px;height:1200px;overflow:hidden;background:#fff}
  body{font-family:"Lato",Arial,sans-serif}
  .flyer{position:relative;width:900px;height:1200px;overflow:hidden;
    background:linear-gradient(90deg,var(--green-deep) 0%,var(--green-mid) 50%,var(--green-bright) 100%)}
  .header{position:absolute;left:0;top:0;width:900px;height:353px;
    background:linear-gradient(180deg,#0c5a3b 0%,#15894c 55%,#1fae57 100%)}
  .header-wave{position:absolute;left:0;top:0}
  .mission{position:absolute;left:80px;top:62px;color:var(--white);font-style:italic;font-weight:700}
  .mission-title{font-size:42px;font-weight:900;line-height:46px}
  .mission-text{font-size:34px;line-height:44px}
  .promise{position:absolute;left:380px;top:258px;width:480px;text-align:center;
    color:var(--ink);font-style:italic;font-size:24px;line-height:31px}
  .process{position:absolute;left:0;top:353px;width:900px;height:55px;
    background:linear-gradient(90deg,var(--gold) 0%,#b8772f 60%,var(--gold-dark) 100%);
    color:var(--white);font-style:italic;font-weight:700;font-size:25px;line-height:55px;text-align:center}
  .left-col{position:absolute;left:60px;top:440px;width:340px;color:var(--white)}
  .section-title{font-size:25px;font-weight:700;line-height:31px}
  .bullets{list-style:none;font-size:16.5px;line-height:21px}
  .bullets li{position:relative;padding-left:20px}
  .bullets li::before{content:"";position:absolute;left:2px;top:7px;width:8px;height:8px;border-radius:50%;background:currentColor}
  .market-list{margin-top:24px}
  .target{position:absolute;left:60px;top:678px;color:var(--white)}
  .target p{font-size:16.5px;line-height:21px;margin-top:14px;padding-left:4px;width:340px}
  .partner{position:absolute;left:60px;top:790px;color:var(--white)}
  .partner .bullets{margin-top:14px;width:340px}
  .partner .bullets li{padding-left:16px}
  .advisor{position:absolute;top:984px;width:144px;text-align:center;color:var(--white)}
  .advisor-photo{width:144px;height:134px;border:2px solid #111;background:linear-gradient(180deg,#e2e2e2,#9d9d9d)}
  .advisor-name{font-size:17px;margin-top:6px}
  .panel{position:absolute;left:428px;top:408px;width:447px;height:426px;background:var(--panel);
    border-radius:0 0 48px 48px}
  .lead{position:absolute;left:471px;top:470px;width:410px;color:var(--ink)}
  .lead-name{font-size:27px;font-weight:700;letter-spacing:.3px}
  .lead .bullets{margin-top:22px;font-size:16.5px}
  .lead .bullets li{padding-left:16px}
  .lead .bullets li::before{top:8px;width:7px;height:7px}
  .team-photo{position:absolute;left:459px;top:787px;width:379px;height:213px;border:4px solid var(--white);
    background:linear-gradient(180deg,#5d6b52 0%,#7d7460 50%,#8a8a84 100%)}
  .contact{position:absolute;left:430px;top:1058px;width:460px;text-align:center;color:var(--white);
    font-style:italic;font-weight:700;font-size:25px;line-height:30px}
  .footer{position:absolute;left:0;top:1162px;width:900px;height:38px;background:var(--footer)}
</style>
</head>
<body>
<main class="flyer">
  <header class="header">
    <svg class="header-wave" width="900" height="353" viewBox="0 0 900 353" aria-hidden="true">
      <defs>
        <linearGradient id="goldLine" x1="0" x2="1">
          <stop offset="0" stop-color="#b8702a"/>
          <stop offset="0.6" stop-color="#e8c08a"/>
          <stop offset="1" stop-color="#f4e2c4" stop-opacity="0.3"/>
        </linearGradient>
        <linearGradient id="ribbon" x1="0" x2="1">
          <stop offset="0" stop-color="#2fbf63"/>
          <stop offset="1" stop-color="#d9f0de"/>
        </linearGradient>
      </defs>
      <path d="M560,222 C700,180 820,195 900,240 L900,270 C820,230 700,215 560,240 Z" fill="url(#ribbon)"/>
      <path d="M0,292 C210,322 420,262 620,228 C760,205 850,220 900,262 L900,353 L0,353 Z" fill="#ffffff"/>
      <path d="M0,280 C200,318 420,248 620,208 C740,185 820,185 870,192" fill="none" stroke="url(#goldLine)" stroke-width="6"/>
      <path d="M0,292 C190,322 380,280 560,248" fill="none" stroke="#0b5a37" stroke-width="5"/>
    </svg>
    <div class="mission">
      <h1 class="mission-title">The Mission:</h1>
      <p class="mission-text">To create a family business by purchasing<br>Multifamily Residences,<br>one at a time.</p>
    </div>
    <p class="promise">To provide a white<br>glove experience to all residences with a<br>clean, safe, and fun environment.</p>
  </header>

  <div class="process">The Process : Buy right, manage right, and finance right</div>

  <section class="left-col">
    <h2 class="section-title">The Market:<br>Colorado Springs</h2>
    <ul class="bullets market-list">
      <li>Projected job growth of nearly 50%</li>
      <li>Below average unemployment rates.</li>
      <li>Above-average incomes.</li>
      <li>Solid economy, military, aerospace, electronics industry, and tourism.</li>
    </ul>
  </section>

  <section class="target">
    <h2 class="section-title">The Target :</h2>
    <p>B and C class assets located in Colorado Springs or nearby submarkets.</p>
  </section>

  <section class="partner">
    <h2 class="section-title">Walt Hollister</h2>
    <ul class="bullets">
      <li>Retired Electrical Engineer.</li>
      <li>Active Real Estate Investor/Consultant.</li>
      <li>Net worth over $4M</li>
      <li>15 Grandchildren.</li>
    </ul>
  </section>

  <figure class="advisor" style="left:62px">
    <div class="advisor-photo" role="img" aria-label="Black and white portrait of advisor Greg Tanner"></div>
    <figcaption class="advisor-name">Greg Tanner</figcaption>
  </figure>
  <figure class="advisor" style="left:235px">
    <div class="advisor-photo" role="img" aria-label="Black and white portrait of advisor Owen Pratt"></div>
    <figcaption class="advisor-name">Owen Pratt</figcaption>
  </figure>

  <div class="panel"></div>
  <section class="lead">
    <h2 class="lead-name">DANE HOLLISTER</h2>
    <ul class="bullets">
      <li>Licensed Colorado Real Estate Agent 18 years.</li>
      <li>Broker-Owner of two Summit Realty Franchises 7 and 2 Years.</li>
      <li>Real Estate investing for 5 years.</li>
      <li>Member of Keystone Income Academy.</li>
      <li>Married 24 years to Marla, parenting 10 children together.</li>
      <li>Appeared on Nate and Leo’s Rental Roundtable podcast Episode 43</li>
      <li>$2M portfolio.</li>
    </ul>
  </section>

  <div class="team-photo" role="img" aria-label="Photo of Dane and Walt Hollister standing together outdoors among trees"></div>

  <address class="contact">Contact:<br>Dane &amp; Walt Hollister 719-555-0148<br>dwhollister@example.com</address>

  <div class="footer"></div>
</main>
</body>
</html>
```